Vision, Mission and Culture Posters

We have written text paragraphs for our company vision and mission and need them made into a2 or a3 sized posters using our logo for inspiration for colour. Our company culture has 10 paragraphs and we'd like this to be a single poster of a2 or a1. Each poster should have the logo on and share common design. It's not a complex job really.

Industry/Entity Type

It Company

Requirements
Nice to have
• These will be going up on our office wall so need to be clear to read from a distance and look professional but also not stodgy.

```html
<!DOCTYPE html>
<html lang="en">
<head>
<meta charset="utf-8">
<title>Bay Spot Hire — Vision and Mission</title>
<link rel="stylesheet" href="https://fonts.googleapis.com/css2?family=Open+Sans:wght@400;700&display=swap">
<style>
  :root {
    --page-bg: #ffffff;
    --brand-yellow: #fff200;
    --brand-ink: #111111;
    --band-red: #b8221c;
    --band-red-light: #ee5a48;
    --band-red-dark: #8e1512;
    --band-red-deep: #a51a17;
    --text-light: #ffffff;
    --sky: #e9ecef;
    --trees: #55684a;
    --cars: #5d6470;
    --asphalt: #3a3b3d;
  }
  * { margin: 0; padding: 0; box-sizing: border-box; }
  html, body { width: 848px; height: 1200px; overflow: hidden; background: var(--page-bg); }
  .poster {
    position: relative;
    width: 848px;
    height: 1200px;
    background: var(--page-bg);
    font-family: "Open Sans", Arial, sans-serif;
    overflow: hidden;
  }
  .brand {
    position: absolute;
    left: 72px;
    top: 110px;
    width: 706px;
    height: 120px;
    display: flex;
    align-items: center;
    gap: 26px;
  }
  .brand-mark {
    width: 86px;
    height: 86px;
    background: var(--brand-yellow);
    flex: none;
  }
  .brand-name {
    font-weight: 700;
    font-size: 60px;
    line-height: 1;
    color: var(--brand-ink);
    letter-spacing: 0.5px;
  }
  .car-park-photo {
    position: absolute;
    left: 0;
    top: 405px;
    width: 848px;
    height: 385px;
    background: linear-gradient(180deg,
      var(--sky) 0%,
      var(--sky) 12%,
      var(--trees) 28%,
      var(--trees) 42%,
      var(--cars) 52%,
      var(--cars) 78%,
      var(--asphalt) 86%,
      var(--asphalt) 100%);
  }
  .statement {
    position: absolute;
    left: 0;
    width: 848px;
    color: var(--text-light);
    padding: 0 69px 0 69px;
  }
  .statement h2 {
    font-weight: 700;
    font-size: 26px;
    line-height: 34px;
    margin-bottom: 6px;
  }
  .statement p {
    font-size: 16.4px;
    line-height: 24px;
    text-align: justify;
    padding-left: 2px;
  }
  .statement--vision {
    top: 790px;
    height: 141px;
    padding-top: 24px;
    background: radial-gradient(ellipse 320px 140px at 42% 45%, var(--band-red-light) 0%, var(--band-red) 70%, var(--band-red-dark) 100%);
  }
  .statement--mission {
    top: 931px;
    height: 269px;
    padding-top: 24px;
    background: radial-gradient(ellipse 520px 240px at 45% 70%, #d4372c 0%, var(--band-red-deep) 60%, var(--band-red-dark) 100%);
    border-top: 2px solid var(--band-red-dark);
  }
  .statement--mission h2 { margin-bottom: 2px; }
</style>
</head>
<body>
  <main class="poster">
    <header class="brand">
      <span class="brand-mark"></span>
      <span class="brand-name">Bay Spot Hire</span>
    </header>

    <div class="car-park-photo" role="img" aria-label="Photograph of a busy open-air car park with rows of parked cars under an overcast sky, trees in the background"></div>

    <section class="statement statement--vision">
      <h2>Our Vission</h2>
      <p>To provide the most hassle-free parking rental service whilst giving a personal customer experience people want to tell their friends about</p>
    </section>

    <section class="statement statement--mission">
      <h2>Our Mission</h2>
      <p>Our mission is to achieve great customer satisfaction in everything we do and offer for meeting our customers’ parking needs. We believe our path to achieving this comes through giving a simple yet thorough and friendly service to our customers without unnecessary complication. We will achieve this through using the technology available to us, continual staff training and development, regular refinement of our practices and processes along with commitment to our roles and the foundations for building our success.</p>
    </section>
  </main>
</body>
</html>
```